Redesign wellness clinic website

The project is redesign a wellness clinic http://www.thornleighvitality.example. The new website is to be responsive,clean,bright and a strong call to action which is to book an appointment. The logo will remain the same but the colour scheme on the website should be reflect purple white and green. I want it to be bright and cheerful and the feeling of clarity. The website shouldn't be overloaded with content but more visuals.

Target Market(s)

Anyone that has corporate wellness benefits within the downtown Toronto core. Majority of audience are professional working in Media, Telecommunications and Investments.

Industry/Entity Type

Health And Wellness

Number of Pages Required

5+ page

Font styles to use
Sans Serif

Colors
ffffff
886aae
acd036

Requirements
Must have
• -Strong call to action which is book an appointment like this page https://www.kestrelmotion.example/
• -Services provided icons on the page like https://www.brightpathvitalityhouse.example/
• - Pictures of a good visualizing a fit and healthy life
• - Strong ratings from Quorva, Zintrel, PostMaz, similar to this website http://www.summitbalancehealth.example/our-team-professionals/
• - Bright and clear
Should not have
• -No black and white images (redo our pictures)
• -Dark themes

```html
<!DOCTYPE html>
<html lang="en">
<head>
<meta charset="utf-8">
<title>Thornleigh Vitality Centre</title>
<link href="https://fonts.googleapis.com/css2?family=Montserrat:wght@400;500;600;700;800&family=Open+Sans:wght@400;600&display=swap" rel="stylesheet">
<style>
:root{
  --white:#ffffff;
  --purple:#886aae;
  --purple-deep:#4b2a7b;
  --purple-dark:#3a1f63;
  --purple-ink:#2a1846;
  --green:#acd036;
  --green-dark:#8fb224;
  --grey-bg:#f4f2f7;
  --text:#555;
  --text-dark:#333;
  --footer:#1d1232;
}
*{margin:0;padding:0;box-sizing:border-box}
html,body{width:1200px;height:4245px;overflow:hidden}
body{font-family:"Open Sans",Arial,sans-serif;color:var(--text);background:var(--white);position:relative}
.section{position:absolute;left:0;width:1200px}
h2,h3,.head{font-family:"Montserrat",Arial,sans-serif}

/* top bar */
.topbar{top:0;height:28px;background:#f2f2f2;font-size:11px;color:#888;display:flex;align-items:center;padding-left:170px;gap:18px}
.topbar span{display:flex;align-items:center;gap:5px}

/* nav */
.nav{top:28px;height:52px;background:var(--white);display:flex;align-items:center;padding:0 0 0 170px;border-bottom:1px solid #eee}
.brand{display:flex;align-items:center;gap:8px;font-family:"Montserrat",sans-serif;font-weight:700;font-size:14px;color:var(--purple-deep)}
.brand i{width:26px;height:26px;border-radius:50%;background:var(--green);display:block}
.menu{display:flex;gap:26px;margin-left:110px;font-family:"Montserrat",sans-serif;font-size:13px;color:#555}
.menu .active{color:var(--purple-deep);font-weight:700}

/* hero */
.hero{top:80px;height:520px;background:linear-gradient(90deg,#e9e4ef 0%,#f5f3f7 40%,#eaeef0 70%,#dfe4e6 100%)}
.hero .photo{position:absolute;inset:0;background:linear-gradient(90deg,rgba(210,190,175,.55),rgba(240,240,242,.2) 45%,rgba(200,205,210,.4))}
.hero-box{position:absolute;left:396px;top:132px;width:410px;text-align:center}
.hero-frame{border:2px solid var(--green);padding:14px 10px 10px}
.hero-kicker{font-family:"Montserrat",sans-serif;font-size:14px;letter-spacing:5px;color:#666}
.hero-title{font-family:"Montserrat",sans-serif;font-weight:800;font-size:52px;line-height:1.05;color:var(--purple-deep);letter-spacing:1px}
.hero-sub{font-family:"Montserrat",sans-serif;font-size:16px;letter-spacing:6px;color:var(--purple-deep)}
.btn{display:inline-block;font-family:"Montserrat",sans-serif;font-weight:600;font-size:14px;letter-spacing:1px;color:var(--white);padding:12px 34px}
.btn-green{background:var(--green)}
.btn-purple{background:var(--purple-deep)}
.hero .btn{margin-top:-2px}
.arrow{position:absolute;top:300px}
.hero-dot{position:absolute;left:576px;top:458px;width:48px;height:48px;border-radius:50%;border:3px solid var(--green);background:rgba(255,255,255,.6)}

/* about */
.about{top:600px;height:660px}
.about-photo{position:absolute;left:100px;top:110px;width:424px;height:424px}
.about-text{position:absolute;left:614px;top:90px;width:470px}
.about h2{font-size:40px;color:var(--green);font-weight:700}
.about h3{font-size:30px;color:var(--purple-ink);font-weight:500;line-height:1.25;margin-bottom:26px}
.about p{font-size:13.5px;line-height:1.75}

/* services */
.services{top:1260px;height:610px;background:linear-gradient(180deg,var(--purple-deep),var(--purple-dark))}
.services h2{position:absolute;top:42px;width:100%;text-align:center;color:var(--white);font-size:38px;font-weight:500}
.services .tag{position:absolute;top:105px;width:100%;text-align:center;color:var(--green);font-size:12px;font-family:"Montserrat",sans-serif}
.card{position:absolute;top:205px;width:270px;height:268px;border:1px solid rgba(255,255,255,.45);padding:100px 28px 0}
.card .icon{position:absolute;top:-24px;left:102px;width:66px;height:66px;border-radius:50%;background:var(--green);border:5px solid rgba(255,255,255,.3)}
.card h3{color:var(--white);font-size:19px;font-weight:500;text-align:center;margin-bottom:24px}
.card ul{list-style:none;color:#fff;font-size:12.5px;line-height:1.75}
.card li::before{content:"";display:inline-block;width:7px;height:7px;background:var(--green);margin-right:8px}
.pager{position:absolute;top:518px;left:532px;display:flex;gap:60px}
.pager i{width:30px;height:30px;border:1px solid var(--green);transform:rotate(45deg);display:block}

/* cta */
.cta{top:1870px;height:225px;background:var(--green);text-align:center;color:var(--white)}
.cta h2{font-size:30px;font-weight:700;margin-top:30px}
.cta p{font-size:22px;line-height:1.35;width:800px;margin:4px auto 20px}

/* testimonial */
.testi{top:2095px;height:525px;background:linear-gradient(180deg,#f1eeee,#fafafa)}
.testi .photo{position:absolute;inset:0;background:linear-gradient(90deg,rgba(225,215,205,.6),rgba(245,245,245,.3),rgba(220,218,214,.6))}
.testi-card{position:absolute;left:218px;top:155px;width:758px;height:270px;background:rgba(255,255,255,.92);border:1px solid #ccc;text-align:center;padding:70px 50px 0}
.avatar{position:absolute;left:328px;top:-45px;width:90px;height:90px;border-radius:50%;background:linear-gradient(#c9d3e0,#8fa3bd);border:4px solid #fff}
.testi-card h3{color:var(--purple-deep);font-size:15px;font-weight:700;margin-bottom:12px}
.testi-card p{font-size:13px;line-height:1.7}

/* hours / booking / video */
.info{top:2620px;height:430px}
.hours{position:absolute;left:0;top:0;width:396px;height:430px;background:var(--purple-deep);color:#fff;padding:34px 36px}
.hours h3{font-weight:500;font-size:20px;text-align:center;margin-bottom:28px}
.hours table{width:100%;font-size:12.5px;border-collapse:collapse}
.hours td{padding:6px 0}
.hours .note{font-size:11.5px;line-height:1.6;margin-top:10px}
.book{position:absolute;left:396px;top:0;width:404px;height:430px;background:var(--purple-dark);color:#fff;padding:34px 40px}
.book h3{font-weight:500;font-size:21px;text-align:center;margin-bottom:40px}
.field{display:inline-block;width:150px;height:38px;border:1px solid rgba(255,255,255,.5);font-size:11px;padding:11px 8px;margin:0 10px 40px 0;color:#ddd}
.book .btn{margin-left:66px}
.video{position:absolute;left:800px;top:0;width:400px;height:430px;background:linear-gradient(135deg,#7e679d,#4b3a66)}
.play{position:absolute;left:170px;top:185px;width:64px;height:64px;border-radius:50%;border:2px solid #fff;background:rgba(255,255,255,.15)}

/* think well */
.think{top:3050px;height:545px;background:#f6f5f8}
.think-text{position:absolute;left:170px;top:80px;width:580px}
.think h2{font-size:34px;color:var(--purple-ink);font-weight:500;margin-bottom:30px}
.think .date{font-size:14px;color:#444;margin-bottom:8px}
.think p{font-size:13px;line-height:1.7}
.think .topic{font-family:"Montserrat",sans-serif;font-weight:700;font-size:13px;color:var(--purple-ink);margin-top:20px}
.dots{display:flex;gap:6px;margin-top:24px}
.dots i{width:28px;height:6px;border-radius:3px;background:#ccc;display:block}
.dots i:first-child{background:var(--purple-deep)}
.think-photo{position:absolute;left:770px;top:40px;width:370px;height:470px}

/* ratings */
.ratings{top:3595px;height:370px;background:var(--white)}
.rate{position:absolute;top:105px;width:235px;height:250px;border:1px solid #ddd;box-shadow:0 2px 8px rgba(0,0,0,.08);display:flex;align-items:center;justify-content:center;flex-direction:column;gap:14px}
.rate .icon{position:absolute;top:-30px;left:88px;width:60px;height:60px;border-radius:50%;background:var(--purple-deep);border:4px solid #fff}
.rate .name{font-family:"Montserrat",sans-serif;font-weight:700;font-size:30px;color:var(--purple-deep)}
.badge{width:110px;height:22px;background:var(--green)}

/* footer */
.footer{top:3965px;height:280px;background:var(--footer);color:#bbb;font-size:12px}
.col{position:absolute;top:32px}
.col h3{color:var(--green);font-size:14px;font-weight:500;margin-bottom:14px;border-bottom:1px solid #444;padding-bottom:8px;width:220px}
.col li{list-style:none;line-height:1.9}
.col p{line-height:1.9}
.footer-video{width:200px;height:150px;background:linear-gradient(135deg,#6e6a75,#3a3640)}
.copy{position:absolute;bottom:0;width:100%;height:26px;border-top:1px solid #333;text-align:center;font-size:11px;line-height:26px;color:#999}
</style>
</head>
<body>

<div class="section topbar">
  <span><svg width="10" height="10" viewBox="0 0 10 10"><path d="M2 1h2l1 2-1 1c.5 1 1 1.5 2 2l1-1 2 1v2c-4 0-7-3-7-7z" fill="#999"/></svg>Phone: 555-014-2290</span>
  <span><svg width="11" height="9" viewBox="0 0 11 9"><rect x=".5" y=".5" width="10" height="8" fill="none" stroke="#999"/><path d="M.5.5l5 4 5-4" fill="none" stroke="#999"/></svg>hello@thornleighvitality.example</span>
</div>

<nav class="section nav">
  <div class="brand"><i></i>Thornleigh Vitality Centre</div>
  <div class="menu">
    <span class="active">[ Home ]</span><span>Fees and Services</span><span>Our Staff</span><span>News and Updates</span><span>Corporate Wellness</span><span>Forms</span><span>Contact</span>
  </div>
</nav>

<header class="section hero">
  <div class="photo" role="img" aria-label="Therapist giving a seated chair massage in a bright clinic"></div>
  <svg class="arrow" style="left:140px" width="20" height="30" viewBox="0 0 20 30"><path d="M16 3L4 15l12 12" fill="none" stroke="#444" stroke-width="3"/></svg>
  <svg class="arrow" style="left:1040px" width="20" height="30" viewBox="0 0 20 30"><path d="M4 3l12 12L4 27" fill="none" stroke="#444" stroke-width="3"/></svg>
  <div class="hero-box">
    <div class="hero-frame">
      <div class="hero-kicker">RELAX &amp; REGENERATE</div>
      <div class="hero-title">THORNLEIGH</div>
      <div class="hero-sub">VITALITY CENTRE</div>
    </div>
    <span class="btn btn-green">BOOK AN APPOINTMENT</span>
  </div>
  <div class="hero-dot"></div>
</header>

<section class="section about">
  <svg class="about-photo" viewBox="0 0 424 424" role="img" aria-label="Physiotherapist stretching a patient's leg on the floor">
    <circle cx="212" cy="212" r="180" fill="none" stroke="#acd036" stroke-width="46"/>
    <rect x="90" y="80" width="300" height="260" fill="#e6dfe9" opacity=".7"/>
  </svg>
  <div class="about-text">
    <h2>ABOUT</h2>
    <h3>THORNLEIGH VITALITY<br>CENTRE</h3>
    <p>Established in 1999 the Thornleigh Vitality Centre has become one of Canada's leaders in providing quality care and innovative wellness programs for the community. The founder and director Dr. Elian Marsh's vision has come to life with over 30 practitioners providing a multitude of different services under one roof. Some of the services include Chiropractic, Physiotherapy, Athletic Therapy, Naturopathy, Massage Therapy, Acupuncture and Personal Training. The Thornleigh Vitality Centre has a complete Pilates studio on its premises. We also offer many wellness seminars free of cost to the public. Our Centre is committed to helping improve and extend the lives of as many people as possible in our community. Come and join our family and start changing your life today.</p>
  </div>
</section>

<section class="section services">
  <h2>OUR SERVICES</h2>
  <div class="tag">THE BEST FOR YOU</div>
  <div class="card" style="left:170px"><span class="icon"></span><h3>CHIROPRACTIC</h3>
    <ul><li>Adjustment</li><li>Functional Adjustment</li><li>Custom Orthotics and Bracing</li></ul></div>
  <div class="card" style="left:467px"><span class="icon"></span><h3>PHYSIOTHERAPY</h3>
    <ul><li>Physiotherapy</li><li>Athletic Therapy</li><li>Custom Orthotics and Bracing</li></ul></div>
  <div class="card" style="left:765px"><span class="icon"></span><h3>ACTIVE REHABILITATION</h3>
    <ul><li>Personal Training</li><li>Pilates</li><li>Fascial Stretch Therapy</li><li>Alexander Technique</li><li>Qigong</li></ul></div>
  <div class="pager"><i></i><i></i></div>
</section>

<section class="section cta">
  <h2>VISIT OUR NEW LOCATION</h2>
  <p>We are open for business at 7:30 am. Open 7 days a week! Ask one of our associates about our Referral Reward Program!</p>
  <span class="btn btn-purple">SEE MAP</span>
</section>

<section class="section testi">
  <div class="photo" role="img" aria-label="Therapist treating a client's shoulder, softly faded"></div>
  <div class="testi-card">
    <div class="avatar" role="img" aria-label="Client portrait"></div>
    <h3>JONAH</h3>
    <p>I attended your clinic recently and was surprised. I am 68 years old and never before was I received so warmly. I believe that natural medicine is the best medicine for all of us. It has fewer and more benign side effects than those created in labs. Your clinic is a real gift for the future of health care. My regret is that most patients are misled by the medical and pharmaceutical powers that be to sway their minds to traditional methods of treating their conditions. I wish all of you, well in your endeavours.</p>
  </div>
</section>

<section class="section info">
  <div class="hours">
    <h3 class="head">OPENING HOURS</h3>
    <table>
      <tr><td>Monday</td><td>7:30am</td><td>-</td><td>8pm</td></tr>
      <tr><td>Tuesday</td><td>7:30am</td><td>-</td><td>8pm</td></tr>
      <tr><td>Wednesday</td><td>7:30am</td><td>-</td><td>8pm</td></tr>
      <tr><td>Thursday</td><td>7:30am</td><td>-</td><td>8pm</td></tr>
      <tr><td>Friday</td><td>7:30am</td><td>-</td><td>8pm</td></tr>
      <tr><td>Saturday</td><td>10am</td><td>-</td><td>3pm</td></tr>
      <tr><td>Sunday</td><td>10am</td><td>-</td><td>3pm</td></tr>
    </table>
    <p class="note">*HOLIDAY HOURS<br>Sat. October 7th, 2017 – OPEN 9:00am – 3:00pm<br>Sun. October 8th, 2017 – OPEN 10:00am – 3:00pm</p>
  </div>
  <div class="book">
    <h3 class="head">Book an Appointment</h3>
    <span class="field">Name*</span><span class="field">Phone*</span>
    <span class="field">Type of Service* ▾</span><span class="field">07/26/2017</span>
    <br><span class="btn btn-green">APPOINTMENT</span>
  </div>
  <div class="video" role="img" aria-label="Video still of a chair massage session">
    <svg class="play" viewBox="0 0 64 64"><path d="M26 20l18 12-18 12z" fill="#fff"/></svg>
  </div>
</section>

<section class="section think">
  <div class="think-text">
    <h2>THINK WELL PROGRAM</h2>
    <div class="date">Monday, June 5, 2017 - 09:29</div>
    <p>Did you know that your mental wellness can directly affect your physical wellness, and vice versa? Our Think Well program comprises Counselling and Sleep Therapy to help you address stress, sleep hygiene, anxiety, depression, family relationships, life transitions, bereavement, and more. Your counsellor will provide a supportive, judgment-free environment and help you build a unique plan to start seeing the changes you are looking for. Depending on your goals and presenting concerns, your counsellor will use various therapy approaches that will work best for you, including Cognitive Behavioural Therapy (CBT) and Mindfulness-Based approaches.</p>
    <div class="topic">Cognitive Behavioural Therapy (CBT)</div>
    <div class="dots"><i></i><i></i><i></i></div>
  </div>
  <svg class="think-photo" viewBox="0 0 370 470" role="img" aria-label="Therapist assisting a patient with a leg stretch">
    <circle cx="200" cy="250" r="150" fill="none" stroke="#acd036" stroke-width="42"/>
    <rect x="40" y="20" width="320" height="400" fill="#e7e3ea" opacity=".75"/>
  </svg>
</section>

<section class="section ratings">
  <div class="rate" style="left:192px"><span class="icon"></span><span class="name">Quorva</span><span class="badge"></span></div>
  <div class="rate" style="left:487px"><span class="icon"></span><span class="name">Zintrel</span><span class="badge"></span></div>
  <div class="rate" style="left:784px"><span class="icon"></span><span class="name">PostMaz</span><span class="badge"></span></div>
</section>

<footer class="section footer">
  <div class="col" style="left:170px"><h3 class="head">Useful Links</h3>
    <ul><li>Home</li><li>Fees and Services</li><li>Our Staff</li><li>News and Updates</li><li>Corporate Wellness</li><li>Forms</li><li>Contact</li></ul></div>
  <div class="col" style="left:467px"><h3 class="head">Contact us</h3>
    <p>Thornleigh Vitality Centre<br>48 Alder Row, Suite 210<br>Toronto ON M0X 0A0</p>
    <p>Phone: 555-014-2290</p><p>Fax: 555-014-2291</p></div>
  <div class="col" style="left:758px"><h3 class="head">Video Review</h3>
    <div class="footer-video" role="img" aria-label="Video review thumbnail"></div></div>
  <div class="copy">© Copyright 2017 thornleighvitality.example</div>
</footer>

</body>
</html>
```